New Phone Case requires logo and packaging

We need a nice and sleek logo designed along with packaging for our Premium Phone Case brand

Our Brand Name is Vaxel
Please note this has nothing to do with a Rhino so don't put a Rhino in the logo
I've also attached a file called VAXEL Logo Inspiration, which shows something along the lines of the type of text we want to use. Please note i have photoshopped that image together from another logo we had, and i liked the text, but its for you to see what direction we want to go in. Also note i have shown different variations in that image file, use your imagination with it and show us a nice and clean logo.

We would like the Brand in upper caps such as VAXEL
The brand is for Premium Phone Cases. The first thing that should come to someones mind when looking at the branding is High Quality, Premium and Modern.

The look must be high end and modern

The design must portray high quality and premium!

Also i will say "Less is More". Don't cramp many things on the packaging and logo. We just want a nice, clean cut high quality logo and packaging

I have attached images of an example packaging from a few competitors. One is a standard open from top packaging, while another is a slide out packaging. Our packaging dimensions should be the same which are Packaging dimensions
Length = 18cm
Height = 1.5cm
Depth = 9.5cm

Also note the example packaging has a transparent front section to show which case is inside, this is optional if you want to have it. If not you can cover it all up.

Font styles to use
Other font styles liked:
• Any nice font but just not the standard everyday stuff like Arial, San Serif etc as i want it to be differentiated. A Font that shows Serious Quality and one that stands out would be awesome!

Colors

Designer to choose colors to be used in the design.

Requirements
Must have
• Must be a nice and clean design
• Packaging dimensions
• Length = 18cm
• Height = 1.5cm
• Depth = 9.5cm

```html
<!DOCTYPE html>
<html lang="en">
<head>
<meta charset="utf-8">
<title>Vaxel – Sleeve Packaging</title>
<link rel="stylesheet" href="https://fonts.googleapis.com/css2?family=Cinzel:wght@500&family=Montserrat:wght@400&display=swap">
<style>
  :root {
    --backdrop: #eef5ee;
    --sleeve: #232323;
    --silver: #a9aaab;
    --ink-light: #f2f2f2;
    --window-top: #f4f4f4;
    --window-mid: #8a8a8a;
    --window-dark: #1c1c1c;
  }
  html, body {
    margin: 0;
    padding: 0;
    width: 1200px;
    height: 2469px;
    overflow: hidden;
    background: var(--backdrop);
  }
  .canvas {
    position: relative;
    width: 1200px;
    height: 2469px;
  }
  .sleeve {
    position: absolute;
    left: 80px;
    top: 348px;
    width: 1040px;
    height: 1773px;
    background: var(--sleeve);
  }
  .product-window {
    position: absolute;
    left: 127px;
    top: 195px;
    width: 277px;
    height: 1369px;
    border-radius: 28px;
    background: linear-gradient(160deg, var(--window-top) 0%, var(--window-mid) 28%, #4a4849 40%, var(--window-dark) 44%, var(--window-dark) 100%);
  }
  .brand-name {
    position: absolute;
    left: 560px;
    width: 470px;
    top: 102px;
    margin: 0;
    text-align: center;
    font-family: "Cinzel", serif;
    font-weight: 500;
    font-size: 104px;
    line-height: 1;
    letter-spacing: 12px;
    color: var(--silver);
  }
  .feature {
    position: absolute;
    left: 627px;
    width: 263px;
    text-align: center;
  }
  .feature svg {
    display: block;
    margin: 0 auto;
  }
  .feature-label {
    display: block;
    font-family: "Montserrat", sans-serif;
    font-size: 25px;
    letter-spacing: 0.5px;
    color: var(--ink-light);
    padding-bottom: 8px;
    border-bottom: 3px solid var(--ink-light);
  }
  .feature--protection { top: 514px; }
  .feature--protection .feature-label { margin-top: 46px; }
  .feature--fit { top: 837px; }
  .feature--fit .feature-label { margin-top: 24px; }
  .tagline {
    position: absolute;
    left: 535px;
    width: 400px;
    top: 1612px;
    margin: 0;
    text-align: center;
    font-family: "Montserrat", sans-serif;
    font-size: 35px;
    line-height: 48px;
    letter-spacing: 1.5px;
    color: var(--ink-light);
  }
</style>
</head>
<body>
<main class="canvas">
  <section class="sleeve">
    <div class="product-window" role="img" aria-label="Clear window showing the phone case inside"></div>

    <h1 class="brand-name">VAXEL</h1>

    <div class="feature feature--protection">
      <svg width="124" height="155" viewBox="0 0 124 155" fill="none" stroke="#f2f2f2" stroke-width="2.5">
        <path d="M2 30 V2 H26 M98 2 H122 V30 M122 125 V153 H98 M26 153 H2 V125"/>
        <rect x="30" y="18" width="64" height="120" rx="10"/>
        <line x1="56" y1="30" x2="70" y2="30"/>
        <circle cx="62" cy="124" r="6"/>
      </svg>
      <span class="feature-label">FULL PROTECTION</span>
    </div>

    <div class="feature feature--fit">
      <svg width="186" height="189" viewBox="0 0 186 189" fill="none" stroke="#f2f2f2" stroke-width="2">
        <line x1="0" y1="30" x2="186" y2="30"/>
        <line x1="0" y1="159" x2="186" y2="159"/>
        <line x1="29" y1="0" x2="29" y2="189"/>
        <line x1="157" y1="0" x2="157" y2="189"/>
        <line x1="70" y1="95" x2="116" y2="95"/>
        <line x1="93" y1="72" x2="93" y2="118"/>
        <circle cx="93" cy="95" r="10" fill="#f2f2f2"/>
      </svg>
      <span class="feature-label">FIT PERFECTLY</span>
    </div>

    <p class="tagline">PREMIUM QUALITY<br>MOBILE ACCESSORIES</p>
  </section>
</main>
</body>
</html>
```